Herbal tea shop web designing - Brewvine

We need a business-charity purpose online shop selling premium herbal teas with a tagline "Healthy with a heart" where all the raw materials are being purchased from Indonesian local farmers in order to give them sustainable employment. Every 20% from the total amount of the customer's purchase from our website always goes back to their communities to help build better sanitation, education or whatever they need. We need page to blog too and another page for customers to interact and share their thought. we expect an eye catching simple earthy (maybe a bit rustic) design with some brush lettering font in some parts. Thank you.

Target Market(s)

-Tea Lovers
-Anyone with body weight issues or any health issues in general

Industry/Entity Type

Home Health Care

Number of Pages Required

5+ page

Font styles to use
Other font styles liked:
• brush lettering font in some parts

Requirements
Must have
• - Brush lettering font
• -Simple, a bit rustic design with some nice watercolor touch
• -Blogging Page
• -catchy yet fancy and elegant E-commerce page
Nice to have
• Well, I will let the designers use their skills and imaginations to the fullest.

```html
<!DOCTYPE html>
<html lang="en">
<head>
<meta charset="utf-8">
<title>Herbal Teas – Blog</title>
<link href="https://fonts.googleapis.com/css2?family=Roboto:wght@300;400;500&family=Playball&display=swap" rel="stylesheet">
<style>
:root{
  --green:#2bb966;
  --green-dark:#23a458;
  --ink:#2b2b2b;
  --muted:#666;
  --line:#e6e6e6;
  --band:#f1f1f1;
  --footer:#2d3037;
  --footer-deep:#24262c;
  --white:#fff;
}
*{box-sizing:border-box;margin:0;padding:0}
html,body{width:936px;height:1200px;overflow:hidden}
body{position:relative;background:var(--white);font-family:"Roboto",sans-serif;color:var(--ink)}
.abs{position:absolute}
svg{display:block}

/* top bar */
.topbar{left:0;top:0;width:936px;height:31px;background:var(--green)}
.social-sq{top:4px;width:23px;height:23px;background:rgba(255,255,255,.18)}
.account-links{right:70px;top:0;height:31px;display:flex}
.account-links a{display:flex;align-items:center;gap:6px;padding:0 14px;color:var(--white);font-size:9px;text-decoration:none;border-left:1px solid rgba(255,255,255,.25)}
.account-links a:last-child{border-right:1px solid rgba(255,255,255,.25)}

/* header */
.brand{left:69px;top:51px;font-size:21px;font-weight:400;color:var(--ink);letter-spacing:.2px}
.main-nav{left:444px;top:57px;display:flex;align-items:center;gap:24px;font-size:10px;color:#444}
.cart{left:824px;top:53px;display:flex;align-items:flex-end;gap:5px;font-size:10px;color:#555}
.cart-badge{left:833px;top:52px;width:12px;height:12px;border-radius:50%;background:var(--green);color:#fff;font-size:7px;text-align:center;line-height:12px}

/* page title */
.title-band{left:0;top:97px;width:936px;height:106px;background:var(--band)}
.page-title{left:69px;top:126px;font-family:"Playball",cursive;font-size:40px;color:#222;line-height:1;font-weight:400}
.crumbs{right:70px;top:144px;font-size:12px;color:#333}
.crumbs span.sep{margin:0 7px}
.crumbs .here{color:var(--green)}

/* blog cards */
.card{width:252px;height:277px;border:1px solid var(--line);background:var(--white)}
.card.active{border-bottom:2px solid var(--green)}
.card-media{position:absolute;left:0;top:0;width:100%;height:163px}
.card-date{position:absolute;left:22px;top:180px;width:40px;text-align:center}
.card-date .day{font-size:22px;font-weight:300;padding-bottom:7px;border-bottom:1px solid var(--line)}
.card-date .mon{font-size:14px;font-weight:300;padding-top:5px}
.card-body{position:absolute;left:71px;top:183px;right:8px}
.card-title{font-size:11.5px;color:#222;margin-left:1px}
.card-time{margin-top:6px;display:flex;align-items:center;gap:5px;font-size:9.5px;color:#555}
.card-text{margin-top:6px;font-size:8.6px;line-height:15px;color:#666}
.learn{margin-top:4px;font-size:9.5px;color:var(--green);display:flex;align-items:center;gap:4px}

/* newsletter */
.news-dark{left:0;top:883px;width:936px;height:280px;background:var(--footer)}
.news-green{left:0;top:876px}
.news-title{left:69px;top:899px;font-size:22px;color:var(--white);font-weight:400}
.news-field{left:490px;top:897px}
.news-input-text{left:543px;top:909px;font-size:10px;color:#999}
.news-btn{left:763px;top:897px;width:103px;height:36px;background:#222429;color:var(--white);font-size:12.5px;text-align:center;line-height:36px}

/* footer */
.f-head{top:980px;font-size:14px;font-weight:500;color:var(--white)}
.f-text{font-size:9.8px;color:#eee;line-height:15px}
.f-links{left:335px;top:1010px;list-style:none;font-size:9.8px;color:#eee}
.f-links li{height:21px}
.f-social{top:1086px;width:20px;height:20px;border-radius:50%;background:rgba(255,255,255,.12)}
.contact-row{left:512px;display:flex;gap:9px;font-size:9.8px;color:#eee;line-height:14px}
.pay{width:36px;height:22px;border-radius:3px}
.bottom-bar{left:0;top:1163px;width:936px;height:37px;background:var(--footer-deep);text-align:center;line-height:37px;font-size:9.8px;color:#eee}
.to-top{left:887px;top:1148px;width:26px;height:26px;border-radius:50%;background:var(--green)}
</style>
</head>
<body>

<div class="abs topbar"></div>
<div class="abs social-sq" style="left:70px"></div>
<div class="abs social-sq" style="left:99px"></div>
<div class="abs social-sq" style="left:127px"></div>
<div class="abs social-sq" style="left:156px"></div>
<div class="abs social-sq" style="left:185px"></div>
<nav class="abs account-links">
  <a><svg width="8" height="9" viewBox="0 0 8 9"><circle cx="4" cy="2.3" r="2.2" fill="#fff"/><path d="M0 9c0-3 1.8-4.3 4-4.3S8 6 8 9z" fill="#fff"/></svg>My Account</a>
  <a><svg width="10" height="9" viewBox="0 0 10 9"><path d="M5 9L1 5C-.5 3.5.3.4 2.6.4 3.7.4 4.5 1 5 1.8 5.5 1 6.3.4 7.4.4 9.7.4 10.5 3.5 9 5z" fill="#fff"/></svg>Wishlist</a>
  <a><svg width="8" height="10" viewBox="0 0 8 10"><rect x="0" y="4" width="8" height="6" fill="#fff"/><path d="M2 4V2.6a2 2 0 0 1 4 0V4" stroke="#fff" stroke-width="1.3" fill="none"/></svg>Log In</a>
  <a><svg width="11" height="10" viewBox="0 0 11 10"><path d="M4 1h6v8H4" stroke="#fff" stroke-width="1.2" fill="none"/><path d="M0 5h6M4 3l2 2-2 2" stroke="#fff" stroke-width="1.2" fill="none"/></svg>Register</a>
</nav>

<div class="abs brand">Herbal Teas</div>
<nav class="abs main-nav">
  <svg width="10" height="9" viewBox="0 0 10 9"><path d="M5 0L0 4.5h1.4V9h2.6V6h2v3h2.6V4.5H10z" fill="#333"/></svg>
  <span style="margin-left:-10px">Shop</span><span>Categories</span><span>Community</span><span>Support</span><span>Contact us</span>
  <svg style="margin-left:2px" width="10" height="10" viewBox="0 0 10 10"><circle cx="4" cy="4" r="3.2" stroke="#777" fill="none"/><path d="M6.4 6.4L9.5 9.5" stroke="#777"/></svg>
</nav>
<div class="abs cart">
  <svg width="15" height="14" viewBox="0 0 15 14"><path d="M0 1h2.5l2 8h8l1.8-6H4" stroke="#444" stroke-width="1.2" fill="none"/><circle cx="5.5" cy="12" r="1.2" fill="#444"/><circle cx="11.5" cy="12" r="1.2" fill="#444"/></svg>Cart
</div>
<div class="abs cart-badge">0</div>

<div class="abs title-band"></div>
<h1 class="abs page-title">Blog</h1>
<div class="abs crumbs">Home<span class="sep">|</span><span class="here">Blog</span></div>

<article class="abs card" style="left:70px;top:252px">
  <div class="card-media" role="img" aria-label="Glass cups of herbal tea with fresh mint leaves" style="background:linear-gradient(135deg,#dcd9c6,#8a9a52 55%,#e9e6de)"></div>
  <div class="card-date"><div class="day">18</div><div class="mon">Jun</div></div>
  <div class="card-body"><div class="card-title">This is Pixelcraft's version of</div>
  <div class="card-time"><svg width="9" height="9" viewBox="0 0 9 9"><circle cx="4.5" cy="4.5" r="3.8" stroke="#2bb966" fill="none"/><path d="M4.5 2.3v2.4h1.8" stroke="#2bb966" fill="none"/></svg>7.30 PM</div>
  <div class="card-text">This is Pixelcraft's version &nbsp;Lorem Ipsum. Proin gravida nibh vel velit auctor aliquet.</div>
  <div class="learn">Learn More <span>»</span></div></div>
</article>
<article class="abs card active" style="left:342px;top:252px">
  <div class="card-media" role="img" aria-label="Steaming dark tea bowl with scattered dried leaves" style="background:linear-gradient(180deg,#5b3a1d,#7c5a36 45%,#6f7a7e)"></div>
  <div class="card-date"><div class="day">03</div><div class="mon">Aug</div></div>
  <div class="card-body"><div class="card-title">This is Pixelcraft's version of</div>
  <div class="card-time"><svg width="9" height="9" viewBox="0 0 9 9"><circle cx="4.5" cy="4.5" r="3.8" stroke="#2bb966" fill="none"/><path d="M4.5 2.3v2.4h1.8" stroke="#2bb966" fill="none"/></svg>7.30 PM</div>
  <div class="card-text">This is Pixelcraft's version &nbsp;Lorem Ipsum. Proin gravida nibh vel velit auctor aliquet.</div>
  <div class="learn">Learn More <span>»</span></div></div>
</article>
<article class="abs card" style="left:614px;top:252px">
  <div class="card-media" role="img" aria-label="Clay pot and ladle full of fresh green sage leaves" style="background:linear-gradient(135deg,#b59a68,#7aa83a 55%,#3f5a1c)"></div>
  <div class="card-date"><div class="day">29</div><div class="mon">May</div></div>
  <div class="card-body"><div class="card-title">This is Pixelcraft's version of</div>
  <div class="card-time"><svg width="9" height="9" viewBox="0 0 9 9"><circle cx="4.5" cy="4.5" r="3.8" stroke="#2bb966" fill="none"/><path d="M4.5 2.3v2.4h1.8" stroke="#2bb966" fill="none"/></svg>7.30 PM</div>
  <div class="card-text">This is Pixelcraft's version &nbsp;Lorem Ipsum. Proin gravida nibh vel velit auctor aliquet.</div>
  <div class="learn">Learn More <span>»</span></div></div>
</article>

<article class="abs card" style="left:70px;top:551px">
  <div class="card-media" role="img" aria-label="White cup of tea on grass surrounded by yellow flowers" style="background:radial-gradient(circle at 50% 45%,#d9a23a,#4f6a26 55%,#3a5220)"></div>
  <div class="card-date"><div class="day">08</div><div class="mon">Jul</div></div>
  <div class="card-body"><div class="card-title">This is Pixelcraft's version of</div>
  <div class="card-time"><svg width="9" height="9" viewBox="0 0 9 9"><circle cx="4.5" cy="4.5" r="3.8" stroke="#2bb966" fill="none"/><path d="M4.5 2.3v2.4h1.8" stroke="#2bb966" fill="none"/></svg>7.30 PM</div>
  <div class="card-text">This is Pixelcraft's version &nbsp;Lorem Ipsum. Proin gravida nibh vel velit auctor aliquet.</div>
  <div class="learn">Learn More <span>»</span></div></div>
</article>
<article class="abs card" style="left:342px;top:551px">
  <div class="card-media" role="img" aria-label="Bundle of fresh thyme and sage with a lemon slice" style="background:linear-gradient(135deg,#e4e2dc,#8c9a73 55%,#dcdad4)"></div>
  <div class="card-date"><div class="day">15</div><div class="mon">Sep</div></div>
  <div class="card-body"><div class="card-title">This is Pixelcraft's version of</div>
  <div class="card-time"><svg width="9" height="9" viewBox="0 0 9 9"><circle cx="4.5" cy="4.5" r="3.8" stroke="#2bb966" fill="none"/><path d="M4.5 2.3v2.4h1.8" stroke="#2bb966" fill="none"/></svg>7.30 PM</div>
  <div class="card-text">This is Pixelcraft's version &nbsp;Lorem Ipsum. Proin gravida nibh vel velit auctor aliquet.</div>
  <div class="learn">Learn More <span>»</span></div></div>
</article>
<article class="abs card" style="left:614px;top:551px">
  <div class="card-media" role="img" aria-label="Yellow teapot pouring into a glass on a garden table" style="background:linear-gradient(135deg,#c8c88c,#e8d96a 45%,#a8b89a)"></div>
  <div class="card-date"><div class="day">25</div><div class="mon">Nov</div></div>
  <div class="card-body"><div class="card-title">This is Pixelcraft's version of</div>
  <div class="card-time"><svg width="9" height="9" viewBox="0 0 9 9"><circle cx="4.5" cy="4.5" r="3.8" stroke="#2bb966" fill="none"/><path d="M4.5 2.3v2.4h1.8" stroke="#2bb966" fill="none"/></svg>7.30 PM</div>
  <div class="card-text">This is Pixelcraft's version &nbsp;Lorem Ipsum. Proin gravida nibh vel velit auctor aliquet.</div>
  <div class="learn">Learn More <span>»</span></div></div>
</article>

<div class="abs news-dark"></div>
<svg class="abs news-green" width="502" height="70" viewBox="0 0 502 70"><polygon points="0,0 439,0 502,70 0,70" fill="#2bb966"/></svg>
<div class="abs news-title">SubscribeTo Our Newsletter</div>
<svg class="abs news-field" width="273" height="36" viewBox="0 0 273 36"><polygon points="0,0 273,0 273,36 34,36" fill="#fff"/></svg>
<svg class="abs" style="left:528px;top:912px" width="10" height="7" viewBox="0 0 10 7"><rect width="10" height="7" fill="#2bb966"/><path d="M0 0l5 4 5-4" stroke="#fff" fill="none"/></svg>
<div class="abs news-input-text">Enter Your Email Address</div>
<div class="abs news-btn">Subscribe</div>

<div class="abs f-head" style="left:70px">Herbal Teas</div>
<p class="abs f-text" style="left:70px;top:1010px;width:190px">This is Pixelcraft's version &nbsp;of Lorem Ipsum proin gravida nibh vel velit auctor aliquet aenean sollicitudin...</p>
<div class="abs learn" style="left:70px;top:1062px">Learn More <span>»</span></div>
<div class="abs f-social" style="left:71px"></div>
<div class="abs f-social" style="left:96px"></div>
<div class="abs f-social" style="left:120px"></div>
<div class="abs f-social" style="left:145px"></div>
<div class="abs f-social" style="left:170px"></div>

<div class="abs f-head" style="left:334px">User Links</div>
<ul class="abs f-links"><li>Home</li><li>Shop</li><li>Categories</li><li>Community</li><li>Support</li><li>Contact us</li></ul>

<div class="abs f-head" style="left:512px">Contact Us</div>
<div class="abs contact-row" style="top:1010px"><svg width="7" height="10" viewBox="0 0 7 10" style="margin-top:3px"><path d="M3.5 10S0 5.6 0 3.5a3.5 3.5 0 0 1 7 0C7 5.6 3.5 10 3.5 10z" fill="#2bb966"/><circle cx="3.5" cy="3.5" r="1.2" fill="#2d3037"/></svg><span>Address Some adress line here,<br>cityname, Country name.</span></div>
<div class="abs contact-row" style="top:1048px"><svg width="9" height="7" viewBox="0 0 9 7" style="margin-top:4px"><rect width="9" height="7" fill="#2bb966"/><path d="M0 0l4.5 3.6L9 0" stroke="#2d3037" fill="none"/></svg><span>Info@example.com</span></div>
<div class="abs contact-row" style="top:1076px"><svg width="9" height="9" viewBox="0 0 9 9" style="margin-top:3px"><path d="M1.8 0l1.6 2.2-1 1.1c.6 1.3 1.6 2.3 2.9 2.9l1.1-1L9 6.8 7.8 9C3.5 8.6.4 5.5 0 1.2z" fill="#2bb966"/></svg><span>+ 123-456-789</span></div>

<div class="abs f-head" style="left:759px">Payment Method</div>
<div class="abs pay" style="left:760px;top:1011px;background:#f4f4f4"></div>
<div class="abs pay" style="left:799px;top:1011px;background:#3a77c8"></div>
<div class="abs pay" style="left:760px;top:1037px;background:#3f8fd8"></div>
<div class="abs pay" style="left:799px;top:1037px;background:#e9e9e9"></div>

<div class="abs bottom-bar">© Copyright All Right Reserved</div>
<div class="abs to-top"><svg width="26" height="26" viewBox="0 0 26 26"><path d="M10 14.5l3-3 3 3" stroke="#fff" stroke-width="1.4" fill="none"/></svg></div>

</body>
</html>
```